Website design using a wordpress template I purchased

I have purchased a wordpress template called "Vantrel" from Plumora and would like to design a website using it for a financial services company. The site simply needs to be informational about the company and a blog. Nothing too involved. The company provides paymaster / escrow services for commodity transactions. I am working on the logo currently and will have it ready to provide shortly. I can provide the content for the informational portion of the site as well. I would like some quick tutoring regarding how to administer the blog portion of the site once built.

```html
<!DOCTYPE html>
<html lang="en">
<head>
<meta charset="utf-8">
<title>Financial Services</title>
<link rel="stylesheet" href="https://fonts.googleapis.com/css2?family=Montserrat:wght@400;500&family=Roboto:wght@400;500;700&display=swap">
<style>
:root{
  --navy:#160a4e;
  --teal:#0a9fc0;
  --badge:#1fb5a5;
  --social:#12aeb2;
  --ink:#2b2b2b;
  --muted:#555;
  --soft-bg:#f9f9f9;
  --card-bg:#f8f7f5;
  --white:#fff;
  --dark:#1a1d22;
}
*{margin:0;padding:0;box-sizing:border-box}
html,body{width:1200px;height:3065px;overflow:hidden}
body{position:relative;background:var(--white);font-family:"Montserrat",sans-serif;color:var(--ink)}
.abs{position:absolute}
.heading{font-family:"Roboto",sans-serif;font-weight:700;color:var(--navy);text-transform:uppercase}
.btn{position:absolute;display:flex;align-items:center;justify-content:center;background:var(--teal);color:var(--white);font-family:"Roboto",sans-serif;font-weight:500;text-transform:uppercase;border-radius:30px;text-decoration:none}

/* hero */
.hero{left:0;top:0;width:1200px;height:566px;background:linear-gradient(135deg,#1f2a3a 0%,#3a3d42 45%,#2b2623 70%,#1b1f27 100%)}
.hero-shade{left:0;top:0;width:1200px;height:566px;background:rgba(10,14,25,.35)}
.nav a{position:absolute;top:25px;color:var(--white);font-family:"Roboto",sans-serif;font-weight:500;font-size:13px;text-decoration:none}
.logo-name{left:0;width:1200px;top:24px;text-align:center;color:var(--white);font-family:"Roboto",sans-serif;font-weight:700;font-size:19px}
.hero-title{left:0;width:1200px;top:196px;text-align:center;color:var(--white);font-size:53px;font-family:"Roboto",sans-serif;font-weight:700}
.hero-text{left:280px;width:640px;top:262px;text-align:center;color:var(--white);font-size:15.5px;line-height:23px}
.hero-btn{left:514px;top:339px;width:172px;height:45px;font-size:17px;border:3px solid var(--white)}
.scroll-tab{left:549px;top:515px;width:102px;height:102px;border-radius:50%;background:var(--white)}

/* about */
.about-title{left:0;width:1200px;top:694px;text-align:center;font-size:52px}
.about-text{left:258px;width:686px;top:775px;text-align:center;font-size:15.5px;line-height:25px;color:var(--muted)}
.about-btn{left:528px;top:923px;width:121px;height:38px;font-size:15px}

.photo-band{left:0;top:1089px;width:1200px;height:385px;background:linear-gradient(120deg,#3b3128 0%,#7e8a99 30%,#c8d3de 50%,#5d6f86 70%,#1f2530 100%)}

/* escrow */
.escrow{left:0;top:1474px;width:1200px;height:571px;background:var(--soft-bg)}
.escrow-title{left:146px;top:1590px;font-size:45px;line-height:53px}
.escrow-text{left:147px;width:480px;top:1722px;font-size:15.5px;line-height:25px;color:var(--muted)}
.escrow-btn{left:149px;top:1942px;width:136px;height:41px;font-size:18px}
.escrow-illustration{left:655px;top:1615px;width:422px;height:322px;background:radial-gradient(ellipse at center,#ececec 0%,#f3f3f3 55%,var(--soft-bg) 100%)}

/* blog */
.blog-band{left:0;top:2045px;width:1200px;height:376px;background:linear-gradient(180deg,#1c2026,#15171b)}
.blog-bottom{left:0;top:2421px;width:1200px;height:290px;background:var(--card-bg)}
.blog-title{left:0;width:1200px;top:2100px;text-align:center;font-size:52px;color:var(--white)}
.blog-intro{left:240px;width:720px;top:2175px;text-align:center;color:var(--white);font-size:15.5px;line-height:24px}
.post-card{position:absolute;top:2265px;width:284px;height:327px;background:var(--white);box-shadow:0 3px 10px rgba(0,0,0,.15)}
.post-image{position:absolute;left:0;top:0;width:284px;height:150px}
.post-date{position:absolute;left:91px;top:132px;width:101px;height:31px;background:var(--badge);color:var(--white);font-family:"Roboto",sans-serif;font-weight:700;font-size:13px;display:flex;align-items:center;justify-content:center}
.post-head{position:absolute;left:21px;top:184px;width:245px;font-family:"Roboto",sans-serif;font-weight:500;font-size:13.5px;line-height:19px;color:#111}
.post-body{position:absolute;left:21px;top:228px;width:240px;font-size:11px;line-height:15px;color:var(--muted)}
.post-link{position:absolute;left:21px;top:282px;font-family:"Roboto",sans-serif;font-weight:500;font-size:13px;color:var(--teal);text-decoration:underline}
.dots{left:573px;top:2637px}

/* footer */
.social{position:absolute;top:2760px;width:41px;height:41px;border-radius:50%;background:var(--social);color:var(--white);font-family:"Roboto",sans-serif;font-weight:500;font-size:8px;display:flex;align-items:center;justify-content:center;text-decoration:none}
.footer-rule{left:89px;top:2843px;width:1041px;height:1px;background:#ddd}
.footer-links{list-style:none;font-family:"Roboto",sans-serif;font-size:15.5px;color:#222}
.footer-links li{height:30px}
.contact-icon{position:absolute;left:806px;width:34px;height:34px;border-radius:50%;background:var(--social)}
.contact-text{position:absolute;left:854px;font-family:"Roboto",sans-serif;font-size:15.5px;line-height:24px;color:#222}
.copyright{left:0;width:1200px;top:3020px;text-align:center;font-family:"Roboto",sans-serif;font-size:11px;color:#222}
</style>
</head>
<body>

<header>
  <div class="abs hero" role="img" aria-label="Photo of business people meeting around a desk with laptop and charts"></div>
  <div class="abs hero-shade"></div>
  <nav class="nav">
    <a style="left:300px" href="#">HOME</a>
    <a style="left:365px" href="#">ABOUT US</a>
    <a style="left:729px" href="#">OUR SERVICES</a>
    <a style="left:846px" href="#">CONTACT US</a>
  </nav>
  <div class="abs logo-name">LOGO NAME</div>
  <h1 class="abs hero-title">FINANCIAL SERVICES</h1>
  <p class="abs hero-text">Lorem ipsum dolor sit amet, consectetur adipiscing elit, sed do eiusmod tempor incididunt ut&nbsp; laboris nisi ut aliquip ex ea commodo consequat.</p>
  <a class="btn hero-btn" href="#">Get Started</a>
  <div class="abs scroll-tab"></div>
  <svg class="abs" style="left:580px;top:548px" width="40" height="40" viewBox="0 0 40 40" fill="none" stroke="#111" stroke-width="2.5"><path d="M3 6 L20 22 L37 6"/><path d="M3 18 L20 34 L37 18"/></svg>
</header>

<section>
  <h2 class="abs heading about-title">About Us</h2>
  <p class="abs about-text">Lorem ipsum dolor sit amet, consectetur adipiscing elit, sed do eiusmod tempor incididunt ut labore et dolore magna aliqua. Ut enim ad minim veniam, quis nostrud exercitation ullamco laboris nisi ut aliquip ex ea commodo consequat. Duis aute irure dolor in reprehenderit in voluptate velit esse cillum dolore eu fugiat nulla pariatur. Excepteur sint occaecat cupidatat non proident, sunt in culpa qui officia deserunt mollit</p>
  <a class="btn about-btn" href="#">Read More</a>
</section>

<div class="abs photo-band" role="img" aria-label="Photo of hands reviewing financial charts with a pen and calculator"></div>

<section>
  <div class="abs escrow"></div>
  <h2 class="abs heading escrow-title">Paymaster/Escrow<br>Services</h2>
  <p class="abs escrow-text">Lorem ipsum dolor sit amet, consectetur adipiscing elit, sed do eiusmod tempor incididunt ut labore et dolore magna aliqua. Ut enim ad minim veniam, quis nostrud exercitation ullamco laboris nisi ut aliquip ex ea commodo consequat. Duis aute irure dolor in reprehenderit in voluptate velit esse cillum dolore eu fugiat nulla pariatur. Excepteur sint occaecat cupidatat non proident, sunt in culpa qui officia deserunt mollit anim id est laborum.</p>
  <a class="btn escrow-btn" href="#">Try Now</a>
  <div class="abs escrow-illustration" role="img" aria-label="Hand-drawn mind map with escrow at the centre linked to broker, agent, contract, payment and related terms"></div>
</section>

<section>
  <div class="abs blog-band" role="img" aria-label="Dark photo of an office workspace"></div>
  <div class="abs blog-bottom"></div>
  <h2 class="abs heading blog-title">Latest Blog</h2>
  <p class="abs blog-intro">Lorem ipsum dolor sit amet, consectetur adipiscing elit, sed do eiusmod tempor incididunt ullamco laboris nisi ut aliquip ex ea commodo consequat.</p>

  <article class="post-card" style="left:147px">
    <div class="post-image" role="img" aria-label="Photo of a person working with financial data on a laptop" style="background:linear-gradient(135deg,#8a5a3a,#2f5d8f 55%,#1c3a66)"></div>
    <div class="post-date">03/10/2022</div>
    <h3 class="post-head">Lorem ipsum dolor sitt, consectetur adipiscing elit, sed do&nbsp; aliqua.</h3>
    <p class="post-body">Lorem ipsum dolor sit amet, consectetur adipiscing elit, sed do eiusmod tempor incididunt ut labore&nbsp; magna aliqua.</p>
    <a class="post-link" href="#">READ MORE</a>
  </article>
  <article class="post-card" style="left:458px">
    <div class="post-image" role="img" aria-label="Photo of two colleagues discussing charts at a desk" style="background:linear-gradient(135deg,#d9dde2,#6f7d92 50%,#2a3550)"></div>
    <div class="post-date">05/10/2022</div>
    <h3 class="post-head">Lorem ipsum dolor sitt, consectetur adipiscing elit, sed do&nbsp; aliqua.</h3>
    <p class="post-body">Lorem ipsum dolor sit amet, consectetur adipiscing elit, sed do eiusmod tempor incididunt ut labore&nbsp; magna aliqua.</p>
    <a class="post-link" href="#">READ MORE</a>
  </article>
  <article class="post-card" style="left:767px">
    <div class="post-image" role="img" aria-label="Photo of a team meeting in a glass office" style="background:linear-gradient(135deg,#9fb6cf,#4e6a8c 50%,#b79b86)"></div>
    <div class="post-date">05/10/2022</div>
    <h3 class="post-head">Lorem ipsum dolor sitt, consectetur adipiscing elit, sed do&nbsp; aliqua.</h3>
    <p class="post-body">Lorem ipsum dolor sit amet, consectetur adipiscing elit, sed do eiusmod tempor incididunt ut labore&nbsp; magna aliqua.</p>
    <a class="post-link" href="#">READ MORE</a>
  </article>

  <svg class="abs dots" width="56" height="16" viewBox="0 0 56 16">
    <circle cx="8" cy="8" r="6.5" fill="none" stroke="#222"/>
    <circle cx="28" cy="8" r="6.5" fill="#111"/>
    <circle cx="48" cy="8" r="6.5" fill="none" stroke="#222"/>
  </svg>
</section>

<footer>
  <a class="social" style="left:520px" href="#">Frendo</a>
  <a class="social" style="left:580px" href="#">Linkwise</a>
  <a class="social" style="left:639px" href="#">Searcha</a>
  <div class="abs footer-rule"></div>
  <ul class="abs footer-links" style="left:152px;top:2876px"><li>About Us</li><li>Meet The Team</li><li>Services</li></ul>
  <ul class="abs footer-links" style="left:452px;top:2876px"><li>Terms &amp; Conditions</li><li>Privacy Policy</li><li>Contact Us</li></ul>
  <div class="contact-icon" style="top:2879px"></div>
  <svg class="abs" style="left:813px;top:2886px" width="20" height="20" viewBox="0 0 20 20"><path d="M10 1 C5.5 1 3 4.3 3 7.8 C3 12.5 10 19 10 19 C10 19 17 12.5 17 7.8 C17 4.3 14.5 1 10 1 Z" fill="#fff"/><circle cx="10" cy="8" r="2.7" fill="var(--social)"/></svg>
  <p class="contact-text" style="top:2875px">123 ipsum dolor sit amet,<br>consectetur adipiscing elit,</p>
  <div class="contact-icon" style="top:2933px"></div>
  <svg class="abs" style="left:813px;top:2940px" width="20" height="20" viewBox="0 0 24 24"><path d="M6.6 10.8c1.4 2.8 3.8 5.1 6.6 6.6l2.2-2.2c.3-.3.7-.4 1-.2 1.1.4 2.3.6 3.6.6.6 0 1 .4 1 1V20c0 .6-.4 1-1 1C10.6 21 3 13.4 3 4c0-.6.4-1 1-1h3.5c.6 0 1 .4 1 1 0 1.3.2 2.5.6 3.6.1.3 0 .7-.2 1L6.6 10.8z" fill="#fff"/></svg>
  <p class="contact-text" style="top:2938px">888 888 8888</p>
  <p class="abs copyright">© Copyright 2022,&nbsp; LOGO&nbsp; All Rights Reserved</p>
</footer>

</body>
</html>
```